Epic Fantasy Book Cover Typography

I have some great cover art for a book cover, but need professional typography added to display the title and author name.

I have included three samples of the book title and author name I did myself in Google Picaso in a few minutes.

Target Market(s)

This will be used on a self-published epic fantasy novel, set in a medieval setting.

Requirements
Must have
• The title must be shown: Bells Under Pale Ruin
The author must be shown: Dermot Fisk

PLEASE USE THE SUPPLIED ARTWORK - I'm only after the typography. However, you are welcome to adjust the colours on the art or modify as required to make the typography stand out. I am open to black and white/sepia too.

```html
<!DOCTYPE html>
<html lang="en">
<head>
<meta charset="utf-8">
<title>Bells Under Pale Ruin — Dermot Fisk</title>
<link rel="stylesheet" href="https://fonts.googleapis.com/css2?family=Almendra:wght@700&family=Metamorphous&display=swap">
<style>
  :root {
    --page-bg: #e9e9e9;
    --cover-dark: #1f1d1b;
    --smoke-top: #2e2a26;
    --smoke: #5a5044;
    --haze: #8c7a58;
    --glow: #f2c23a;
    --glow-hot: #fff4b8;
    --ember: #c9861e;
    --ground: #3a2e22;
    --ground-dark: #1a1714;
    --author-gold: #f1b52e;
    --metal-light: #f4f1e8;
    --metal-mid: #b9b3a4;
    --metal-dark: #6f695d;
    --metal-shade: #8f887a;
  }
  html, body {
    margin: 0;
    width: 1200px;
    height: 900px;
    overflow: hidden;
    background: var(--page-bg);
  }
  .book-cover {
    position: absolute;
    left: 310px;
    top: 30px;
    width: 580px;
    height: 840px;
    overflow: hidden;
    background: var(--cover-dark);
  }
  .cover-art {
    position: absolute;
    inset: 0;
    background:
      radial-gradient(ellipse 30% 12% at 40% 50%, var(--glow-hot) 0%, rgba(255,244,184,0) 100%),
      radial-gradient(ellipse 60% 26% at 38% 48%, var(--glow) 0%, rgba(242,194,58,0.55) 40%, rgba(242,194,58,0) 80%),
      radial-gradient(ellipse 70% 30% at 55% 30%, rgba(110,98,80,0.7) 0%, rgba(110,98,80,0) 80%),
      radial-gradient(ellipse 40% 18% at 88% 58%, rgba(20,18,16,0.6) 0%, rgba(20,18,16,0) 100%),
      radial-gradient(ellipse 65% 30% at 35% 70%, rgba(122,84,40,0.75) 0%, rgba(122,84,40,0) 80%),
      linear-gradient(180deg, var(--smoke-top) 0%, var(--smoke) 20%, var(--haze) 38%, var(--ember) 50%, var(--ground) 64%, #2a2420 80%, var(--ground-dark) 100%);
  }
  .author-name {
    position: absolute;
    top: 112px;
    left: 0;
    right: 0;
    margin: 0;
    text-align: center;
    padding-left: 70px;
    font-family: "Almendra", serif;
    font-weight: 700;
    font-size: 42px;
    letter-spacing: 1px;
    color: var(--author-gold);
    text-shadow: 1px 2px 3px rgba(0,0,0,0.6);
  }
  .book-title {
    position: absolute;
    left: 34px;
    top: 500px;
    margin: 0;
    font-family: "Metamorphous", serif;
    font-weight: 400;
    font-size: 58px;
    line-height: 1.15;
    letter-spacing: 1px;
    text-transform: uppercase;
    white-space: nowrap;
    filter: drop-shadow(2px 3px 2px rgba(0,0,0,0.85));
  }
  .book-title .title-line {
    display: block;
    color: transparent;
    background:
      repeating-linear-gradient(100deg, rgba(255,255,255,0.12) 0 2px, rgba(0,0,0,0.08) 2px 5px),
      linear-gradient(180deg, var(--metal-light) 0%, var(--metal-mid) 38%, var(--metal-dark) 50%, var(--metal-shade) 62%, var(--metal-light) 100%);
    -webkit-background-clip: text;
    background-clip: text;
    -webkit-text-stroke: 0.6px rgba(60,55,48,0.9);
  }
  .book-title .title-line--second { padding-left: 40px; }
</style>
</head>
<body>
  <main class="book-cover">
    <div class="cover-art" role="img" aria-label="Cover artwork: a hooded swordswoman with a flaming blade standing on a mound of skulls before a burning golden sky and a ruined city in the clouds"></div>
    <p class="author-name">Dermot Fisk</p>
    <h1 class="book-title">
      <span class="title-line">Bells Under</span>
      <span class="title-line title-line--second">Pale Ruin</span>
    </h1>
  </main>
</body>
</html>
```